Business Card Design

We are a radiology group

We are working to move into new service centers

We want to communicate innovation and bringing our customers ahead with technology and outstanding results

I have uploaded a high resolution logo as requested :-)

Target Market(s)

hospitals, clinics

Industry/Entity Type

Business

Contact Information for Business Card

Linda R. Feathersby, MBA, CIIP
CTIO
linda.feathersby@trovexa-rad.com
cell 607-481-2937
www.trovexa-rad.com
Trovexa Radiology Partners, PC

```html
<!DOCTYPE html>
<html lang="en">
<head>
<meta charset="utf-8">
<title>Trovexa Radiology Partners – Business Card</title>
<link rel="stylesheet" href="https://fonts.googleapis.com/css2?family=Ubuntu:wght@400;500&display=swap">
<style>
  :root {
    --page-bg: #e9ebee;
    --card-white: #ffffff;
    --navy: #16303f;
    --sky: #7fb0d3;
    --ink: #1f2f3a;
    --scan-dark: #142331;
    --scan-mid: #3f6178;
    --scan-light: #a8c6da;
  }
  * { margin: 0; padding: 0; box-sizing: border-box; }
  html, body {
    width: 1200px; height: 1023px; overflow: hidden;
    background: var(--page-bg);
    font-family: "Ubuntu", Arial, sans-serif;
  }
  .business-card {
    position: absolute;
    left: 160px; top: 260px;
    width: 880px; height: 504px;
    background: var(--card-white);
    border-radius: 24px;
    overflow: hidden;
    box-shadow: 0 14px 40px rgba(20, 40, 60, 0.18);
  }
  .scan-band { position: absolute; left: 0; top: 0; width: 880px; height: 504px; }
  .holder-name {
    position: absolute; right: 48px; top: 20px; text-align: right;
  }
  .holder-name .name {
    font-size: 30px; font-weight: 500; color: var(--navy); letter-spacing: 0.2px;
  }
  .holder-name .credentials {
    font-size: 19px; color: var(--sky); margin-top: 2px;
  }
  .brand-block {
    position: absolute; left: 40px; top: 180px; width: 190px;
    display: flex; align-items: center; gap: 10px;
  }
  .brand-dot {
    flex: none; width: 14px; height: 14px; border-radius: 50%; background: var(--sky);
  }
  .brand-name {
    font-size: 17px; font-weight: 500; color: var(--ink);
    text-transform: uppercase; line-height: 1.25; letter-spacing: 0.4px;
  }
  .office {
    position: absolute; left: 210px; top: 336px; line-height: 1.22;
  }
  .office .company {
    font-size: 20px; color: var(--sky); text-transform: uppercase; letter-spacing: 0.3px;
  }
  .office .address { font-size: 20px; color: var(--ink); }
  .contact-list {
    position: absolute; right: 48px; top: 336px; text-align: right;
    list-style: none; line-height: 1.26; font-size: 19px; color: var(--ink);
  }
  .contact-list .tag { color: var(--sky); font-weight: 500; margin-right: 6px; }
  .accent-line {
    position: absolute; left: 0; right: 0; top: 438px; height: 8px; background: var(--sky);
  }
  .footer-bar {
    position: absolute; left: 0; right: 0; top: 454px; height: 50px; background: var(--navy);
  }
</style>
</head>
<body>
  <div class="business-card">
    <svg class="scan-band" viewBox="0 0 880 504" role="img" aria-label="Band of blue-toned brain MRI scan images">
      <defs>
        <linearGradient id="scanTone" x1="0" y1="0" x2="1" y2="1">
          <stop offset="0" stop-color="var(--scan-light)"/>
          <stop offset="0.45" stop-color="var(--scan-mid)"/>
          <stop offset="1" stop-color="var(--scan-dark)"/>
        </linearGradient>
      </defs>
      <polygon points="300,96 880,96 880,318 210,318" fill="url(#scanTone)"/>
    </svg>

    <div class="holder-name">
      <div class="name">Linda R. Feathersby</div>
      <div class="credentials">MBA, CIIP CTIO</div>
    </div>

    <div class="brand-block">
      <span class="brand-dot"></span>
      <span class="brand-name">Trovexa Radiology Partners</span>
    </div>

    <div class="office">
      <div class="company">Trovexa Radiology Partners</div>
      <div class="address">27 Ridgeline Drive, Suite 4</div>
      <div class="address">Elmira, NY 14901</div>
    </div>

    <ul class="contact-list">
      <li><span class="tag">[M]</span>607-481-2937</li>
      <li><span class="tag">[E]</span>linda.feathersby@trovexa-rad.com</li>
      <li><span class="tag">[W]</span>www.trovexa-rad.com</li>
    </ul>

    <div class="accent-line"></div>
    <div class="footer-bar"></div>
  </div>
</body>
</html>
```